USB Business Card Design
Pelham Trowbridge Partners Chartered Accountants
Simple
Marcus Trowbridge, CA
Partner
20418-127 Ave
Edmonton, AB
T6K 4M3
T:855.316.2084
P:780.316.2084, D: 780.552.7391
F:780.317.6058
MTrowbridge@ptpca.com
www.ptpca.com
This is going to be printed onto a Business card sized USB stick. They are 2 sided, flashy and plastic coated. This is for extremely high end clients and need to look really amazing! We are open to all ideas, the bosses are partial to a simple look.

```html
<!DOCTYPE html>
<html lang="en">
<head>
<meta charset="utf-8">
<title>Pelham Trowbridge Partners – Business Card</title>
<link rel="stylesheet" href="https://fonts.googleapis.com/css2?family=Open+Sans:ital,wght@0,400;0,600;0,700;1,600&display=swap">
<style>
  :root {
    --navy: #1d3a7a;
    --navy-deep: #16306a;
    --gold: #d99a1e;
    --paper: #ffffff;
    --ink: #5a6478;
    --backdrop: #eceef2;
  }
  * { box-sizing: border-box; margin: 0; padding: 0; }
  html, body { width: 1200px; height: 980px; overflow: hidden; }
  body {
    background: var(--backdrop);
    font-family: "Open Sans", Arial, sans-serif;
    display: flex;
    flex-direction: column;
    align-items: center;
    justify-content: center;
    gap: 40px;
  }
  .card {
    position: relative;
    width: 760px;
    height: 434px;
    border-radius: 18px;
    overflow: hidden;
    box-shadow: 0 6px 18px rgba(20, 30, 60, 0.18);
  }
  .card-front { background: var(--paper); }
  .card-back { background: var(--navy); }

  .front-swoosh { position: absolute; inset: 0; }

  .firm-name {
    position: absolute;
    left: 48px;
    top: 40px;
    display: flex;
    align-items: center;
    gap: 14px;
    color: var(--navy);
    font-weight: 700;
    font-size: 26px;
    line-height: 1.15;
  }
  .firm-name .mark {
    width: 44px; height: 44px;
    background: var(--navy);
    flex: none;
  }
  .firm-name small { display: block; font-size: 26px; }

  .contact-list {
    position: absolute;
    left: 48px;
    top: 150px;
    list-style: none;
    color: var(--ink);
    font-size: 14px;
    line-height: 1;
  }
  .contact-list li {
    display: flex;
    align-items: center;
    gap: 10px;
    height: 25px;
  }
  .contact-list .icon { width: 16px; height: 16px; flex: none; }
  .contact-list .spacer { width: 16px; flex: none; }

  .holder {
    position: absolute;
    right: 130px;
    top: 306px;
    text-align: right;
    color: var(--navy);
  }
  .holder-name { font-size: 22px; font-weight: 600; font-style: italic; }
  .holder-title { font-size: 14px; color: var(--ink); margin-top: 4px; }

  .back-name {
    position: absolute;
    left: 60px;
    top: 60px;
    display: flex;
    align-items: center;
    gap: 16px;
    color: var(--paper);
    font-weight: 700;
    font-size: 30px;
    line-height: 1.15;
  }
  .back-name .mark { width: 54px; height: 54px; background: var(--gold); flex: none; }
  .back-url {
    position: absolute;
    right: 60px;
    bottom: 110px;
    color: var(--paper);
    font-size: 20px;
    letter-spacing: 0.42em;
  }
</style>
</head>
<body>

<section class="card card-front" aria-label="Card front">
  <svg class="front-swoosh" viewBox="0 0 760 434" aria-hidden="true">
    <path d="M760,60 C748,220 705,362 600,434 L760,434 Z" fill="var(--navy)"/>
    <path d="M728,34 C720,206 664,352 556,434" fill="none" stroke="var(--navy)" stroke-width="7"/>
  </svg>

  <div class="firm-name">
    <span class="mark"></span>
    <span>Pelham Trowbridge Partners<small>Chartered Accountants</small></span>
  </div>

  <ul class="contact-list">
    <li>
      <svg class="icon" viewBox="0 0 16 16" aria-hidden="true"><circle cx="8" cy="8" r="8" fill="var(--navy)"/><path d="M8 3.5a3 3 0 0 1 3 3c0 2.2-3 6-3 6s-3-3.8-3-6a3 3 0 0 1 3-3z" fill="#fff"/><circle cx="8" cy="6.5" r="1.1" fill="var(--navy)"/></svg>
      20418-127 Ave
    </li>
    <li><span class="spacer"></span>Edmonton, AB T6K 4M3</li>
    <li>
      <svg class="icon" viewBox="0 0 16 16" aria-hidden="true"><circle cx="8" cy="8" r="8" fill="var(--navy)"/><path d="M5.2 4h2l.8 2-1.2.9a5 5 0 0 0 2.3 2.3L10 8l2 .8v2c0 .6-.5 1-1 1A7 7 0 0 1 4.2 5c0-.5.4-1 1-1z" fill="#fff"/></svg>
      T: 855.316.2084
    </li>
    <li>
      <svg class="icon" viewBox="0 0 16 16" aria-hidden="true"><circle cx="8" cy="8" r="8" fill="var(--navy)"/><path d="M5.2 4h2l.8 2-1.2.9a5 5 0 0 0 2.3 2.3L10 8l2 .8v2c0 .6-.5 1-1 1A7 7 0 0 1 4.2 5c0-.5.4-1 1-1z" fill="#fff"/></svg>
      P: 780.316.2084
    </li>
    <li>
      <svg class="icon" viewBox="0 0 16 16" aria-hidden="true"><circle cx="8" cy="8" r="8" fill="var(--navy)"/><path d="M5.2 4h2l.8 2-1.2.9a5 5 0 0 0 2.3 2.3L10 8l2 .8v2c0 .6-.5 1-1 1A7 7 0 0 1 4.2 5c0-.5.4-1 1-1z" fill="#fff"/></svg>
      D: 780.552.7391
    </li>
    <li>
      <svg class="icon" viewBox="0 0 16 16" aria-hidden="true"><circle cx="8" cy="8" r="8" fill="var(--navy)"/><rect x="4.5" y="6.5" width="7" height="4.5" fill="#fff"/><rect x="6" y="4.2" width="4" height="2.3" fill="#fff"/></svg>
      F: 780.317.6058
    </li>
    <li>
      <svg class="icon" viewBox="0 0 16 16" aria-hidden="true"><circle cx="8" cy="8" r="8" fill="var(--navy)"/><rect x="4" y="5" width="8" height="6" fill="#fff"/><path d="M4 5l4 3.3L12 5" fill="none" stroke="var(--navy)" stroke-width="1"/></svg>
      MTrowbridge@ptpca.com
    </li>
    <li>
      <svg class="icon" viewBox="0 0 16 16" aria-hidden="true"><circle cx="8" cy="8" r="8" fill="var(--navy)"/><circle cx="8" cy="8" r="4" fill="none" stroke="#fff" stroke-width="1.1"/><path d="M4 8h8M8 4c-1.6 2.2-1.6 5.8 0 8M8 4c1.6 2.2 1.6 5.8 0 8" fill="none" stroke="#fff" stroke-width="0.9"/></svg>
      www.ptpca.com
    </li>
  </ul>

  <div class="holder">
    <p class="holder-name">Marcus Trowbridge, CA</p>
    <p class="holder-title">Partner</p>
  </div>
</section>

<section class="card card-back" aria-label="Card back">
  <div class="back-name">
    <span class="mark"></span>
    <span>Pelham Trowbridge Partners</span>
  </div>
  <p class="back-url">www.ptpca.com</p>
</section>

</body>
</html>
```